"The Plum Principle" Book Cover Design

Name of book: The Plum Principle

Tagline: Exploring 8 essential truths to living and loving more deeply.

Author: Rosalinda Ferrando-Vega

Size: 5in w x 8in h Paperback

This is the second book of 30 year old Entrepreneur, Author and Speaker. The book basically tells the story of her youth and immigrating to the United States at 14.

"The Plum Principle" name came about since she started selling figs outside her home in mexico city... Her family had a fig three in their backyard, and when she was about 6 she had the courage of starting her own business.

Here is the Book Description:
At some point in our lives, we all face the question: Does crisis and pain propel us forward or put our lives on hold? In this deeply intimate memoir, Rosalinda Ferrando Vega shares the eight hidden secrets—the fig factors as she calls them—of discovering true awareness and embracing life’s big sky possibilities, even amidst our greatest struggles.

The Plum Principle is an emotionally-charged story spanning two countries and three decades. Vega expertly takes our hand and invites us to walk with her. We begin in her homeland of Mexico as she recounts her mother’s unrelenting faith in giving birth to a little girl, the good that came from the arsonist’s flames devouring her childhood home and the life-changing discovery she encountered after watching her father walk away again and again with a bottle in his hand. Her immigration to the United States as a young teenager and the amazing medical discovery that both saved her life while nearly taking it away offer true inspiration that the human spirit dictates triumph in the lives of everyday people.

Vega clearly touches our hearts in this beautifully written, very personal memoir, showing us how to find more to every moment of living through love, awareness, forgiveness, gratitude and more. Each chapter is capped off with thought-provoking questions underscoring Vega’ real message: the answers to life’s greatest questions lie within each of us.
Updates

The author's favorite colors are Purple, Lime Green, and Black...  notice that Figs are also purple

Target Market(s)

Mostly women but men should also get interested in reading book

Industry/Entity Type

Medical

Requirements
Must have
• Title, tagline, and author's name;

The Plum Principle

Exploring the 8 essential truths to living and loving more deeply

Rosalinda Ferrando-Vega

```html
<!DOCTYPE html>
<html lang="en">
<head>
<meta charset="utf-8">
<title>The Plum Principle — Cover</title>
<link href="https://fonts.googleapis.com/css2?family=Permanent+Marker&family=Kalam:wght@400&display=swap" rel="stylesheet">
<style>
  :root {
    --stage: #1b1a1c;
    --mist-light: #cfd4d0;
    --mist-mid: #8d9591;
    --forest-shade: #47444a;
    --forest-floor: #241f24;
    --plum: #5b2a6e;
    --plum-deep: #2e1536;
    --lime: #a4d233;
    --ink: #121212;
  }
  html, body {
    margin: 0;
    padding: 0;
    width: 1200px;
    height: 796px;
    overflow: hidden;
    background: var(--stage);
  }
  .stage {
    position: relative;
    width: 1200px;
    height: 796px;
    display: flex;
    align-items: center;
    justify-content: center;
  }
  .cover {
    position: relative;
    width: 498px;
    height: 796px;
    overflow: hidden;
  }
  .cover__forest {
    position: absolute;
    inset: 0;
    background:
      radial-gradient(ellipse 70% 35% at 60% 20%, var(--mist-light) 0%, rgba(207,212,208,0.5) 45%, rgba(207,212,208,0) 80%),
      linear-gradient(180deg, var(--mist-mid) 0%, #727a76 35%, var(--forest-shade) 62%, var(--forest-floor) 100%);
  }
  .cover__plum-wash {
    position: absolute;
    inset: 0;
    background: linear-gradient(180deg, rgba(91,42,110,0) 45%, rgba(91,42,110,0.45) 78%, rgba(46,21,54,0.85) 100%);
  }
  .cover__text {
    position: absolute;
    right: 30px;
    top: 170px;
    width: 438px;
    text-align: right;
  }
  .cover__title {
    margin: 0;
    font-family: "Permanent Marker", "Kalam", cursive;
    font-weight: 400;
    font-size: 56px;
    line-height: 1.05;
    letter-spacing: 2px;
    color: var(--ink);
    text-transform: uppercase;
  }
  .cover__rule {
    display: block;
    width: 120px;
    height: 4px;
    margin: 18px 0 16px auto;
    background: var(--lime);
  }
  .cover__tagline {
    margin: 0 0 0 auto;
    max-width: 340px;
    font-family: "Kalam", cursive;
    font-size: 20px;
    line-height: 1.3;
    color: var(--plum-deep);
  }
  .cover__author {
    position: absolute;
    right: 30px;
    bottom: 46px;
    margin: 0;
    font-family: "Permanent Marker", "Kalam", cursive;
    font-size: 22px;
    line-height: 1;
    letter-spacing: 1.5px;
    color: var(--lime);
    text-transform: uppercase;
    white-space: nowrap;
  }
</style>
</head>
<body>
  <div class="stage">
    <main class="cover">
      <div class="cover__forest" role="img" aria-label="Photograph of a misty forest with twisting dark tree trunks and a leaf-covered path"></div>
      <div class="cover__plum-wash"></div>
      <div class="cover__text">
        <h1 class="cover__title">The Plum<br>Principle</h1>
        <span class="cover__rule"></span>
        <p class="cover__tagline">Exploring the 8 essential truths to living and loving more deeply</p>
      </div>
      <p class="cover__author">Rosalinda Ferrando-Vega</p>
    </main>
  </div>
</body>
</html>
```